Business card for partnership

Plumbing and hvac company needing a minimal business card. We already have a logo i would like the front of the card just the logo and the back have all info.

Target Market(s)

Commercial facilities

Industry/Entity Type

Plumbing hvac

Contact Information for Business Card

We would like it double sided. Logo big and bold on the front and out info on the back. Our info on back would be name and position phone, email, and location

```html
<!DOCTYPE html>
<html lang="en">
<head>
<meta charset="utf-8">
<title>Kestrel Mechanical – Business Card</title>
<link rel="stylesheet" href="https://fonts.googleapis.com/css2?family=Open+Sans:wght@400;700;800&display=swap">
<style>
  :root {
    --bg: #e4e5e7;
    --card-dark: #333333;
    --orange-deep: #e4521b;
    --orange-bright: #f7931e;
    --edge: #111111;
    --white: #ffffff;
    --ink: #222222;
  }
  * { margin: 0; padding: 0; box-sizing: border-box; }
  html, body { width: 1200px; height: 800px; overflow: hidden; }
  body {
    background: var(--bg);
    font-family: "Open Sans", Arial, sans-serif;
    position: relative;
  }
  .card {
    position: absolute;
    top: 250px;
    width: 520px;
    height: 300px;
    background: var(--card-dark);
    overflow: hidden;
    box-shadow: 0 10px 24px rgba(0,0,0,0.18);
  }
  .card--back { left: 50px; }
  .card--front { left: 630px; }
  .card__wave { position: absolute; inset: 0; width: 100%; height: 100%; }

  .wordmark {
    position: absolute;
    color: var(--white);
    font-weight: 800;
    text-transform: uppercase;
    line-height: 0.95;
    letter-spacing: 0.02em;
  }
  .wordmark__main { display: block; font-size: 1em; }
  .wordmark__sub { display: block; font-size: 0.46em; letter-spacing: 0.08em; }
  .card--back .wordmark { right: 30px; bottom: 30px; font-size: 54px; text-align: left; }
  .card--front .wordmark { left: 70px; top: 100px; font-size: 66px; }

  .holder { position: absolute; left: 30px; top: 24px; color: var(--ink); }
  .holder__name { font-weight: 800; font-size: 17px; letter-spacing: 0.02em; text-transform: uppercase; }
  .holder__role { font-size: 12px; }

  .contact-list { position: absolute; left: 30px; top: 120px; list-style: none; color: var(--white); font-size: 14px; }
  .contact-list li { display: flex; align-items: flex-start; gap: 9px; margin-bottom: 6px; line-height: 1.25; }
  .contact-list .address { margin-top: 14px; }
  .contact-list svg { width: 13px; height: 13px; flex: none; margin-top: 2px; fill: var(--orange-bright); }
</style>
</head>
<body>

<section class="card card--back" aria-label="Card back with contact details">
  <svg class="card__wave" viewBox="0 0 520 300" preserveAspectRatio="none" aria-hidden="true">
    <defs>
      <linearGradient id="waveBack" x1="0" y1="0" x2="1" y2="1">
        <stop offset="0" stop-color="var(--orange-deep)"/>
        <stop offset="1" stop-color="var(--orange-bright)"/>
      </linearGradient>
    </defs>
    <path d="M0,0 H520 V190 C440,192 370,150 300,118 C210,78 100,86 0,92 Z" fill="url(#waveBack)"/>
    <path d="M0,92 C100,86 210,78 300,118 C370,150 440,192 520,190" fill="none" stroke="var(--edge)" stroke-width="5"/>
  </svg>

  <div class="holder">
    <div class="holder__name">Dana Reyes</div>
    <div class="holder__role">Director</div>
  </div>

  <ul class="contact-list">
    <li><svg viewBox="0 0 16 16"><path d="M3 1h3l1.5 4-2 1.2a9 9 0 0 0 4.3 4.3L11 8.5l4 1.5v3a2 2 0 0 1-2 2A13 13 0 0 1 1 3a2 2 0 0 1 2-2z"/></svg>555-014-2273</li>
    <li><svg viewBox="0 0 16 16"><path d="M1 3h14v10H1z M1 3l7 6 7-6" fill="none" stroke="var(--orange-bright)" stroke-width="2"/></svg>info@kestrelmechanical.com</li>
    <li><svg viewBox="0 0 16 16"><circle cx="8" cy="8" r="6.5" fill="none" stroke="var(--orange-bright)" stroke-width="1.8"/><path d="M1.5 8h13M8 1.5c-3 3.5-3 9.5 0 13M8 1.5c3 3.5 3 9.5 0 13" fill="none" stroke="var(--orange-bright)" stroke-width="1.4"/></svg>www.kestrelmechanical.com</li>
    <li class="address"><svg viewBox="0 0 16 16"><path d="M8 0a5.5 5.5 0 0 0-5.5 5.5C2.5 10 8 16 8 16s5.5-6 5.5-10.5A5.5 5.5 0 0 0 8 0zm0 8a2.5 2.5 0 1 1 0-5 2.5 2.5 0 0 1 0 5z"/></svg><span>99 dummy city<br>dummy place 0000</span></li>
  </ul>

  <div class="wordmark">
    <span class="wordmark__main">Kestrel</span>
    <span class="wordmark__sub">Mechanical</span>
  </div>
</section>

<section class="card card--front" aria-label="Card front with company name">
  <svg class="card__wave" viewBox="0 0 520 300" preserveAspectRatio="none" aria-hidden="true">
    <defs>
      <linearGradient id="waveFront" x1="0" y1="0" x2="1" y2="1">
        <stop offset="0" stop-color="var(--orange-bright)"/>
        <stop offset="0.6" stop-color="var(--orange-deep)"/>
        <stop offset="1" stop-color="var(--orange-bright)"/>
      </linearGradient>
    </defs>
    <path d="M160,0 H520 V255 C470,256 440,210 410,168 C360,98 260,105 215,62 C190,38 175,18 160,0 Z" fill="url(#waveFront)"/>
    <path d="M160,0 C175,18 190,38 215,62 C260,105 360,98 410,168 C440,210 470,256 520,255" fill="none" stroke="var(--edge)" stroke-width="5"/>
  </svg>

  <div class="wordmark">
    <span class="wordmark__main">Kestrel</span>
    <span class="wordmark__sub">Mechanical</span>
  </div>
</section>

</body>
</html>
```